Aviation: Overcast Study Guide Book Cover

We need a book cover (front and back) designed for an Instrument Flight Rules (IFR) study guide used by helicopter and airplane pilots to obtain an instrument rating for a helicopter or airplane. Below is the title and subtitles.

TITLE: OVERCAST STUDY GUIDE
SUBTITLE 1: Checkride Preparation for Airplane and Helicopter Pilots
SUBTITLE 2: Prepare for your Instrument Rating with Confidence

We have also upload recommended text to be included on the back cover. In addition, we included images of similar book covers that we like and ones that we do not like. Below are links to two others books by the author.

https://www.bookvarro.example/Rotorcraft-Exam-Handbook-oral-review/dp/507214638K
https://www.bookvarro.example/Manual-Floatwing-Handling-Lionel-Quarrick/dp/5093742816

Flight students

Aviation

• helicopter and airplane

```html
<!DOCTYPE html>
<html lang="en">
<head>
<meta charset="utf-8">
<title>Overcast Study Guide – Cover Spread</title>
<link href="https://fonts.googleapis.com/css2?family=Bebas+Neue&family=Teko:wght@400;500&family=Montserrat:wght@600;700&display=swap" rel="stylesheet">
<style>
  :root {
    --cover-red: #d0232a;
    --paper-white: #ffffff;
    --backdrop: #eeeeee;
    --cockpit-dark: #1f1a17;
    --sky-light: #c9dde4;
    --water-blue: #7ea9bd;
  }
  * { margin: 0; padding: 0; box-sizing: border-box; }
  html, body { width: 900px; height: 1200px; overflow: hidden; background: var(--backdrop); }
  .canvas { position: relative; width: 900px; height: 1200px; }
  .cover-spread {
    position: absolute; left: 0; top: 264px; width: 900px; height: 671px;
    background: var(--cover-red); overflow: hidden; color: var(--paper-white);
  }
  .white-band { position: absolute; left: 0; top: 525px; width: 900px; height: 34px; background: var(--paper-white); }
  .heading {
    position: absolute; left: 61px; font-family: "Teko", sans-serif; font-weight: 400;
    font-size: 18px; line-height: 1; letter-spacing: 0.1px;
  }
  .body-copy {
    position: absolute; left: 61px; width: 356px; font-family: "Montserrat", sans-serif;
    font-weight: 700; font-size: 7.6px; line-height: 1.36;
  }
  .topic-list {
    position: absolute; top: 286px; left: 98px; width: 320px; display: grid;
    grid-template-columns: repeat(3, 101px); row-gap: 2px;
    font-family: "Teko", sans-serif; font-size: 11px; line-height: 1.2; list-style: none;
  }
  .about-box {
    position: absolute; left: 56px; top: 346px; width: 371px; height: 138px;
    background: var(--paper-white); border-radius: 10px; color: #111; padding: 6px 6px 0 6px;
  }
  .about-title { font-family: "Teko", sans-serif; font-weight: 500; font-size: 16px; line-height: 1; }
  .about-text { margin-top: 9px; font-family: "Montserrat", sans-serif; font-weight: 700; font-size: 7.4px; line-height: 1.3; }
  .spine {
    position: absolute; left: 434px; top: 0; width: 35px; height: 525px;
  }
  .spine-title, .spine-author {
    position: absolute; left: 50%; transform: translateX(-50%); writing-mode: vertical-rl;
    white-space: nowrap;
  }
  .spine-title { top: 155px; font-family: "Bebas Neue", sans-serif; font-size: 19px; }
  .spine-author { top: 327px; font-family: "Montserrat", sans-serif; font-weight: 700; font-size: 14px; letter-spacing: 0.5px; }
  .front { position: absolute; left: 469px; top: 0; width: 431px; height: 671px; }
  .front-title {
    position: absolute; top: 56px; width: 100%; left: -10px; text-align: center;
    font-family: "Bebas Neue", sans-serif; font-size: 56px; line-height: 1; white-space: nowrap;
  }
  .front-subtitle {
    position: absolute; top: 121px; width: 100%; left: -10px; text-align: center;
    font-family: "Montserrat", sans-serif; font-weight: 600; font-size: 15.5px; line-height: 1.3;
  }
  .cockpit-photo {
    position: absolute; top: 187px; left: 0; width: 431px; height: 338px;
    background: linear-gradient(180deg, var(--sky-light) 0%, var(--water-blue) 30%, #5c5a50 50%, var(--cockpit-dark) 70%, #120f0d 100%);
  }
  .cockpit-strip { position: absolute; top: 559px; left: 0; width: 431px; height: 18px; background: var(--cockpit-dark); }
  .front-author {
    position: absolute; top: 525px; width: 100%; left: -10px; height: 34px; line-height: 34px; text-align: center;
    font-family: "Montserrat", sans-serif; font-weight: 700; font-size: 17px; color: var(--cover-red); letter-spacing: 0.3px;
  }
  .front-tagline {
    position: absolute; top: 606px; width: 100%; left: -10px; text-align: center;
    font-family: "Teko", sans-serif; font-weight: 500; font-size: 21px; line-height: 1;
  }
</style>
</head>
<body>
<div class="canvas">
  <section class="cover-spread">
    <div class="white-band"></div>

    <div class="back-cover">
      <h2 class="heading" style="top:95px;">Prepare for your IFR check ride with confidence</h2>
      <p class="body-copy" style="top:126px;">Becoming an instrument rated pilot is one of the most challenging ratings to obtain. This guide helps prepare you to pass your IFR check ride with confidence. The question-and-answer format is easy to follow and provides detailed explanations for expanded knowledge.</p>
      <h2 class="heading" style="top:188px;">Includes Helicopter and Airplane Specific Content</h2>
      <p class="body-copy" style="top:220px;">This guide is designed to prepare an airplane or helicopter pilot the oral portion of the IFR checkride. Unlike other resources, this guide specifically addresses the differences with IFR flight in helicopters. As a dual rated pilot, the author ensures to identify areas of differences between the two categories of IFR flight. The following concepts are addressed within the guide.</p>
      <ul class="topic-list">
        <li>•Preflight Actions</li><li>•Enroute Procedures</li><li>•Aeromedical Factors</li>
        <li>•General IFR Concepts</li><li>•Approach Procedures</li><li>•Weather Fundamentals</li>
        <li>•Departure Procedures</li><li>•IFR Emergencies</li><li>•Risk Management</li>
      </ul>
      <div class="about-box">
        <h3 class="about-title">ABOUT THE AUTHOR:</h3>
        <p class="about-text">Lionel Quarrick is ATP rated pilot and helicopter and fixed-wing instructor. Lionel is the owner and operator Bearing Line, LLC which does business as Hover Point Aviation and Pike Water Aviation. Hover Point Aviation provides primary helicopter flight instruction while Pike Water Aviation provides seaplane flight instruction and tours. In addition to instructing, Lionel has authored other books to include The Rotorcraft Exam Handbook, and Manual of Floatwing Handling. Lionel lives in Ohio with his beautiful wife Maren. They have a daughter, Tessa, that is dual rated and employed as a captain for a charter company. Prior to learning to fly, Lionel spent several years in the military as a Special Warfare Combat Craft Crewman in the U.S. Navy and Ranger-qualified infantry officer in the U.S. Army.</p>
      </div>
    </div>

    <div class="spine">
      <span class="spine-title">OVERCAST STUDY GUIDE</span>
      <span class="spine-author">LIONEL J. QUARRICK</span>
    </div>

    <div class="front">
      <h1 class="front-title">OVERCAST STUDY GUIDE</h1>
      <p class="front-subtitle">Checkride Preparation for<br>Airplane and Helicopter Pilots</p>
      <div class="cockpit-photo" role="img" aria-label="Photo of a small airplane cockpit instrument panel with a pilot's hand on the yoke, coastline and water seen through the windscreen"></div>
      <div class="front-author">LIONEL J. QUARRICK</div>
      <div class="cockpit-strip"></div>
      <p class="front-tagline">Prepare for your Instrument Rating with Confidence</p>
    </div>
  </section>
</div>
</body>
</html>
```